Promotional Post crad

SEE SAMPLE POST CARD <br/><br/>Everything in our lab is manufactured inhouse. No outsourcing !<br/><br/>FULL SERVICE DIGITAL DENTAL LABORATORY<br/><br/>We restore all implants <br/><br/>Implant packages starting from $499<br/><br/>Full contour zirconia crown $99<br/><br/>Build up zirconia crown $179<br/><br/>Implant package promotion starting at 499<br/><br/>Try to make the same design on the back of the card with different parts adding up to the final product

Target Market(s)

Dentists

```html
<!DOCTYPE html>
<html lang="en">
<head>
<meta charset="utf-8">
<title>Harbor Dental Laboratory – Postcard</title>
<link href="https://fonts.googleapis.com/css2?family=Libre+Baskerville:wght@400;700&family=Montserrat:wght@300;400;600;700&family=Oswald:wght@500&display=swap" rel="stylesheet">
<style>
  :root{
    --blue:#1b87cf;
    --blue-deep:#136fb0;
    --blue-soft:#4aa3e0;
    --charcoal:#3b3b3b;
    --grey:#5a5a5a;
    --light:#e9e9e9;
    --white:#ffffff;
    --sans:'Montserrat', Arial, sans-serif;
    --serif:'Libre Baskerville', Georgia, serif;
    --cond:'Oswald', 'Arial Narrow', sans-serif;
  }
  *{box-sizing:border-box;margin:0;padding:0}
  html,body{width:706px;height:1200px;overflow:hidden;background:var(--white)}
  .canvas{position:relative;width:706px;height:1200px;overflow:hidden;background:var(--white)}
  .card{position:absolute;left:65px;width:578px;height:385px;overflow:hidden;background:var(--white);box-shadow:0 2px 6px rgba(0,0,0,.28)}
  .card--front{top:212px}
  .card--back{top:643px}
  .card__art{position:absolute;inset:0;width:578px;height:385px}
  .abs{position:absolute}

  /* brand */
  .brand{display:flex;align-items:center;gap:7px}
  .brand__dot{width:22px;height:22px;border:2px solid var(--blue);border-radius:50%}
  .brand__name{font-family:var(--serif);font-weight:700;color:var(--blue);line-height:1.05}
  .brand__name span{display:block}
  .brand--front{left:262px;top:26px}
  .brand--front .brand__name{font-size:27px}
  .brand--front .brand__name span+span{font-size:15px}
  .brand--back{left:345px;top:46px;gap:5px}
  .brand--back .brand__dot{width:14px;height:14px;border-width:1.5px}
  .brand--back .brand__name{font-size:14px}
  .brand--back .brand__name span+span{font-size:8px}

  /* front */
  .claim{left:288px;top:125px;width:270px;text-align:center;color:var(--white);font-family:var(--sans);font-weight:300;font-size:13px;line-height:1.2;letter-spacing:.2px}
  .headline{left:290px;top:160px;width:270px;text-align:center;color:var(--white);font-family:var(--serif);font-weight:700;font-size:20px;white-space:nowrap}
  .headline-pill{left:294px;top:182px;width:262px;height:26px;border-radius:13px;background:linear-gradient(#ffffff,#c9c9c9);box-shadow:0 1px 3px rgba(0,0,0,.35);display:flex;align-items:center;justify-content:center;font-family:var(--serif);font-weight:700;font-size:19px;color:var(--grey);white-space:nowrap}
  .promo-label{left:301px;top:216px;color:var(--white);font-family:var(--cond);font-weight:500;font-size:15.5px;line-height:1.05;text-transform:uppercase}
  .restore{left:474px;top:223px;color:var(--white);font-family:var(--sans);font-weight:700;font-size:10.5px;line-height:1.25}
  .call-label{font-family:var(--sans);font-weight:600;font-size:13px}
  .front-call{left:303px;top:287px;color:var(--grey)}
  .front-phone{left:303px;top:300px;display:flex;align-items:center;gap:4px;color:var(--grey);font-family:var(--sans);font-weight:700;font-size:24px;letter-spacing:.5px}
  .front-mail{left:303px;top:330px;display:flex;align-items:center;gap:6px;color:var(--grey);font-family:var(--sans);font-size:10.5px}
  .web-bar{left:240px;top:343px;width:269px;height:26px;border-radius:0 13px 13px 0;background:var(--blue-deep);display:flex;align-items:center;justify-content:center;gap:6px;color:var(--white);font-family:var(--sans);font-weight:600;font-size:10px;letter-spacing:1.6px}
  .social{top:350px;width:12px;height:12px;border:1.6px solid var(--blue-deep);border-radius:50%}
  .social--one{left:514px}
  .social--two{left:542px}

  /* back */
  .offer-label{left:41px;top:29px;font-family:var(--serif);font-size:9.5px;color:var(--charcoal)}
  .offer-price{left:190px;top:29px;font-family:var(--serif);font-weight:700;font-size:26px;color:var(--blue)}
  .services{left:39px;top:112px;color:var(--white);font-family:var(--serif);font-size:6.4px;line-height:1.35}
  .services__title{font-weight:700;margin-bottom:2px}
  .services__cols{display:flex;gap:18px}
  .services ul{list-style:none}
  .services li::before{content:"";display:inline-block;width:3px;height:3px;border:0.8px solid var(--white);border-radius:50%;margin-right:3px;vertical-align:middle}
  .price-card{width:62px;text-align:center;font-family:var(--serif);font-size:7px;line-height:1.3;color:var(--charcoal);transform:translate(-50%,-50%);top:245px}
  .price-card--a{left:67px}
  .price-card--b{left:145px}
  .price-card--c{left:223px}
  .price-tag{top:289px;transform:translate(-50%,-50%);font-family:var(--serif);font-weight:700;font-size:12.5px;color:var(--white)}
  .price-tag--a{left:67px}
  .price-tag--b{left:145px}
  .price-tag--c{left:223px}
  .back-call{left:79px;top:321px;color:var(--white)}
  .back-phone{left:81px;top:331px;display:flex;align-items:center;gap:4px;color:var(--white);font-family:var(--sans);font-weight:700;font-size:25px;letter-spacing:.5px}
  .back-contact{left:81px;top:360px;display:flex;align-items:center;gap:6px;color:var(--white);font-family:var(--sans);font-size:7px}
  .back-contact .gap{margin-left:8px}
</style>
</head>
<body>
<div class="canvas">

  <!-- FRONT -->
  <section class="card card--front">
    <svg class="card__art" viewBox="0 0 1214 809" preserveAspectRatio="none">
      <defs>
        <linearGradient id="photoTone" x1="0" y1="0" x2="1" y2="1">
          <stop offset="0" stop-color="#dfe3e8"/>
          <stop offset=".55" stop-color="#c9b3a6"/>
          <stop offset="1" stop-color="#8a8f96"/>
        </linearGradient>
        <radialGradient id="retainerTone" cx=".5" cy=".45" r=".6">
          <stop offset="0" stop-color="#e0504e"/>
          <stop offset=".6" stop-color="#c9c9cc"/>
          <stop offset="1" stop-color="#23252b"/>
        </radialGradient>
      </defs>
      <!-- blue wave field -->
      <path fill="#1b87cf" d="M0,74 C200,40 420,70 560,150 C700,225 820,250 900,248 C1020,240 1120,215 1214,175 L1214,715 C1140,650 1060,560 1000,548 C880,540 760,545 690,575 C610,620 570,720 545,809 L0,809 Z"/>
      <!-- dark swoosh under logo -->
      <path fill="#3b3b3b" d="M888,246 C1010,236 1120,200 1214,128 L1214,176 C1120,218 1010,245 888,246 Z"/>
      <!-- dark swoosh along contact panel -->
      <path fill="#3b3b3b" d="M450,809 C520,690 560,600 690,560 C780,535 880,535 1000,545 C880,548 770,560 700,600 C620,650 580,730 555,809 Z"/>
      <!-- white contact panel -->
      <path fill="#ffffff" d="M560,809 C585,730 625,655 700,605 C770,565 880,552 1000,552 C1070,560 1140,640 1214,715 L1214,809 Z"/>
      <!-- main photograph -->
      <path role="img" aria-label="Smiling patient in a dental chair holding a denture model" fill="url(#photoTone)" d="M0,86 C170,60 360,90 470,210 C560,300 610,420 605,540 C590,640 520,730 450,809 L0,809 Z"/>
      <!-- retainer photograph -->
      <circle cx="1100" cy="627" r="86" fill="#ffffff"/>
      <circle role="img" aria-label="Orthodontic retainer on a stone model" cx="1100" cy="627" r="80" fill="url(#retainerTone)"/>
      <!-- implant icon -->
      <circle cx="935" cy="492" r="42" fill="none" stroke="#ffffff" stroke-width="3"/>
      <g fill="none" stroke="#ffffff" stroke-width="2.5">
        <rect x="920" y="465" width="26" height="14" rx="5"/>
        <path d="M926,479 L929,498 L937,498 L940,479"/>
        <rect x="910" y="496" width="50" height="22" rx="6"/>
        <path d="M922,500 v14 M935,500 v14 M948,500 v14"/>
      </g>
    </svg>

    <div class="abs brand brand--front">
      <span class="brand__dot"></span>
      <div class="brand__name"><span>HARBOR</span><span>Dental Laboratory</span></div>
    </div>

    <p class="abs claim">Everything in our lab is manufactured inhouse. No outsourcing !</p>
    <h1 class="abs headline">FULL SERVICE DIGITAL</h1>
    <div class="abs headline-pill">DENTAL LABORATORY</div>
    <p class="abs promo-label">Implant Package<br>Promotions</p>
    <p class="abs restore">We restore<br>all implants</p>

    <p class="abs call-label front-call">Call Us Now</p>
    <p class="abs front-phone">
      <svg width="11" height="11" viewBox="0 0 24 24"><path fill="#1b87cf" d="M6.6 10.8a15 15 0 0 0 6.6 6.6l2.2-2.2c.3-.3.7-.4 1-.2 1.1.4 2.3.6 3.6.6.6 0 1 .4 1 1V20c0 .6-.4 1-1 1A17 17 0 0 1 3 4c0-.6.4-1 1-1h3.5c.6 0 1 .4 1 1 0 1.3.2 2.5.6 3.6.1.3 0 .7-.2 1z"/></svg>
      555 014 2280
    </p>
    <p class="abs front-mail">
      <svg width="10" height="8" viewBox="0 0 20 14"><rect width="20" height="14" rx="1" fill="#1b87cf"/><path d="M1,1 L10,8 L19,1" fill="none" stroke="#fff" stroke-width="1.6"/></svg>
      harbordental@example.com
    </p>
    <div class="abs web-bar">
      <svg width="10" height="10" viewBox="0 0 20 20"><g fill="none" stroke="#fff" stroke-width="1.5"><circle cx="10" cy="10" r="8.5"/><ellipse cx="10" cy="10" rx="4" ry="8.5"/><path d="M1.5 10h17M3 5.5h14M3 14.5h14"/></g></svg>
      www.harbordentallab.com
    </div>
    <span class="abs social social--one"></span>
    <span class="abs social social--two"></span>
  </section>

  <!-- BACK -->
  <section class="card card--back">
    <svg class="card__art" viewBox="0 0 1214 809" preserveAspectRatio="none">
      <defs>
        <linearGradient id="faintTone" x1="0" y1="0" x2="0" y2="1">
          <stop offset="0" stop-color="#ffffff"/>
          <stop offset="1" stop-color="#efefef"/>
        </linearGradient>
        <radialGradient id="pearl" cx=".5" cy=".4" r=".6">
          <stop offset="0" stop-color="#ffffff"/>
          <stop offset="1" stop-color="#e3e3e3"/>
        </radialGradient>
        <linearGradient id="smileTone" x1="0" y1="0" x2="1" y2="0">
          <stop offset="0" stop-color="#1b87cf" stop-opacity="0"/>
          <stop offset="1" stop-color="#0f5f9c"/>
        </linearGradient>
      </defs>
      <rect width="1214" height="809" fill="#1b87cf"/>
      <!-- soft smile photo behind price circles -->
      <path role="img" aria-label="Close-up of a bright smile in blue tone" fill="url(#smileTone)" opacity=".6" d="M360,470 C450,430 620,440 700,500 L700,650 L360,650 Z"/>
      <!-- white address side -->
      <path fill="#ffffff" d="M985,0 L1214,0 L1214,809 L665,809 C705,720 700,560 635,440 C575,310 640,80 985,0 Z"/>
      <!-- dark crescent -->
      <path fill="#3b3b3b" d="M960,8 C700,80 610,280 660,430 C710,570 760,690 780,809 L800,809 C790,690 745,570 700,430 C650,280 730,90 960,8 Z"/>
      <!-- faint portrait area -->
      <rect role="img" aria-label="Faded portrait of a smiling woman" x="795" y="430" width="395" height="379" fill="url(#faintTone)"/>
      <!-- stamp -->
      <rect x="1056" y="73" width="117" height="118" rx="4" fill="#e8e8e8" stroke="#bdbdbd" stroke-width="2"/>
      <!-- address lines -->
      <g stroke="#c8c8c8" stroke-width="2">
        <line x1="811" y1="438" x2="1173" y2="438"/>
        <line x1="811" y1="488" x2="1173" y2="488"/>
        <line x1="811" y1="540" x2="1173" y2="540"/>
        <line x1="811" y1="595" x2="1173" y2="595"/>
      </g>
      <!-- offer box -->
      <path d="M45,110 V326 Q45,338 57,338 H555 V300" fill="none" stroke="#ffffff" stroke-width="2" stroke-dasharray="3 4"/>
      <rect x="63" y="51" width="485" height="270" rx="22" fill="none" stroke="#ffffff" stroke-width="4"/>
      <path fill="#ffffff" d="M85,51 H526 Q548,51 548,73 V110 Q548,128 530,128 H410 Q390,128 380,98 H63 V73 Q63,51 85,51 Z"/>
      <!-- brand badge -->
      <rect x="80" y="157" width="83" height="34" rx="3" fill="#ffffff"/>
      <!-- component photos -->
      <g stroke="#ffffff" stroke-width="4">
        <circle role="img" aria-label="Implant abutment on model" cx="216" cy="171" r="32" fill="#c9c6c0"/>
        <circle role="img" aria-label="Custom abutment" cx="302" cy="171" r="32" fill="#d8cfc3"/>
        <circle role="img" aria-label="Zirconia crown on model" cx="391" cy="171" r="32" fill="#b89a80"/>
        <circle role="img" aria-label="Finished implant restoration" cx="477" cy="171" r="32" fill="#5e5e62"/>
      </g>
      <g fill="#ffffff" font-family="Montserrat, Arial, sans-serif" font-size="26" text-anchor="middle">
        <text x="259" y="180">+</text><text x="346" y="180">+</text><text x="434" y="180">+</text>
      </g>
      <!-- denture photo -->
      <ellipse role="img" aria-label="Full acrylic denture" cx="530" cy="282" rx="70" ry="52" fill="#e9a08e"/>
      <!-- connector -->
      <path d="M306,338 V425" stroke="#ffffff" stroke-width="2" stroke-dasharray="3 4"/>
      <circle cx="306" cy="338" r="5" fill="#ffffff"/>
      <circle cx="306" cy="423" r="5" fill="#ffffff"/>
      <!-- partner badges -->
      <g fill="#ffffff">
        <rect x="110" y="363" width="100" height="40" rx="3"/>
        <rect x="256" y="363" width="100" height="40" rx="3"/>
        <rect x="392" y="363" width="100" height="40" rx="3"/>
      </g>
      <!-- dotted arcs -->
      <path d="M48,515 C48,410 200,395 222,470 C250,400 360,400 386,470 C412,400 560,410 560,515" fill="none" stroke="#ffffff" stroke-width="2" stroke-dasharray="3 4"/>
      <circle cx="48" cy="515" r="5" fill="#ffffff"/>
      <circle cx="560" cy="515" r="5" fill="#ffffff"/>
      <circle cx="222" cy="472" r="5" fill="#ffffff"/>
      <circle cx="386" cy="472" r="5" fill="#ffffff"/>
      <!-- price circles -->
      <g>
        <circle cx="140" cy="514" r="82" fill="#4aa3e0"/>
        <circle cx="304" cy="514" r="82" fill="#4aa3e0"/>
        <circle cx="468" cy="514" r="82" fill="#4aa3e0"/>
        <circle cx="140" cy="514" r="70" fill="url(#pearl)"/>
        <circle cx="304" cy="514" r="70" fill="url(#pearl)"/>
        <circle cx="468" cy="514" r="70" fill="url(#pearl)"/>
        <g fill="#3b3b3b" stroke="#ffffff" stroke-width="4">
          <circle cx="140" cy="607" r="35"/>
          <circle cx="304" cy="607" r="35"/>
          <circle cx="468" cy="607" r="35"/>
        </g>
      </g>
      <!-- bottom contact band -->
      <path fill="#3b3b3b" d="M0,745 C60,690 170,660 420,652 L728,645 C722,720 705,770 684,809 L0,809 Z"/>
      <rect role="img" aria-label="Stained ceramic crowns on model" x="25" y="660" width="125" height="110" rx="14" fill="#d9c39a"/>
    </svg>

    <div class="abs brand brand--back">
      <span class="brand__dot"></span>
      <div class="brand__name"><span>HARBOR</span><span>Dental Laboratory</span></div>
    </div>

    <p class="abs offer-label">Implant packages starting from</p>
    <p class="abs offer-price">$499</p>

    <div class="abs services">
      <p class="services__title">Services:</p>
      <div class="services__cols">
        <ul><li>Crown &amp; Bridge</li><li>Implants</li><li>Digital Connection</li></ul>
        <ul><li>Orthodontic</li><li>Full &amp; Partial Dentures</li></ul>
      </div>
    </div>

    <p class="abs price-card price-card--a">FULL<br>CONTOUR<br>ZIRCONIA<br>CROWN</p>
    <p class="abs price-card price-card--b">BUILD UP<br>ZIRCONIA<br>CROWN</p>
    <p class="abs price-card price-card--c">IMPLANT<br>PACKAGE<br>PROMOTION<br>STARTING<br>AT</p>
    <p class="abs price-tag price-tag--a">$99</p>
    <p class="abs price-tag price-tag--b">$179</p>
    <p class="abs price-tag price-tag--c">$499</p>

    <p class="abs call-label back-call">Call Us Now</p>
    <p class="abs back-phone">
      <svg width="9" height="9" viewBox="0 0 24 24"><path fill="#4aa3e0" d="M6.6 10.8a15 15 0 0 0 6.6 6.6l2.2-2.2c.3-.3.7-.4 1-.2 1.1.4 2.3.6 3.6.6.6 0 1 .4 1 1V20c0 .6-.4 1-1 1A17 17 0 0 1 3 4c0-.6.4-1 1-1h3.5c.6 0 1 .4 1 1 0 1.3.2 2.5.6 3.6.1.3 0 .7-.2 1z"/></svg>
      555 014 2280
    </p>
    <p class="abs back-contact">
      <svg width="7" height="5" viewBox="0 0 20 14"><rect width="20" height="14" rx="1" fill="#4aa3e0"/></svg>
      harbordental@example.com
      <svg class="gap" width="6" height="6" viewBox="0 0 20 20"><circle cx="10" cy="10" r="8.5" fill="none" stroke="#fff" stroke-width="2"/></svg>
      www.harbordentallab.com
    </p>
  </section>

</div>
</body>
</html>
```